Website Design for my CNC machine Shop.

I need a new website for my Machining Company.

It can be a simple website that acts more like an "Online Business card" I has to highlight the services I provide and give Companies the confidence to engage my services.

I needs it to be a really modern or even a little futuristic promoting my Company.

I have just moved locations and have renovated the premises and would be great to let everyone know along with a new website.

If you can help with linking it to search engines to help get more exposure that would be great.

It needs to accommodate the three main services I provide which will include capacities of each machine (within that service) and maybe a couple images.
CNC Machining (5-axis, 3-axis)
EDM Wire cutting
3D Metal Printing
Along with home page and Contact page

I have two websites and you can use the txt from either/combination of these.
www.korvaltooling.com.au
(no longer do Laser Marking and etching but now do 3D metal Printing)
www.tarnquill.com.au

Happy to chat further with the designer

Company logo's provided.

For Images: I am happy to use Glimmerbay and can purchase any images you like
EDM Wire cut
https://www.glimmerbay-pics.com/search/edm-wire-cutting

CNC Machining:
https://www.glimmerbay-pics.com/search/vertical-cnc-machining
Don't use any with engines or motor vehicle parts

3D metal Printing
https://www.glimmerbay-pics.com/search/slm-metal-printing

Target Market(s)

Defence, Aerospace, Medical, HIgh Precision

Industry/Entity Type

Mechanical Engineering

Coding

Coded - Design and coding required

Number of Pages Required

5+ page

Requirements
Must have
• Home page, 3 services, Contacts. Can add image to each of the services

```html
<!DOCTYPE html>
<html lang="en">
<head>
<meta charset="utf-8">
<title>Korval Precision Machinists</title>
<link href="https://fonts.googleapis.com/css2?family=Poppins:wght@400;500;600&family=Inter:wght@400;500&display=swap" rel="stylesheet">
<style>
:root{
  --green:#34bc8a;
  --navy:#0f2a3c;
  --mint:#e6f5f0;
  --text:#4a5560;
  --white:#ffffff;
}
*{box-sizing:border-box;margin:0;padding:0}
html,body{width:1200px;height:2421px;overflow:hidden}
body{position:relative;font-family:Inter,Arial,sans-serif;color:var(--text);background:var(--white)}
.abs{position:absolute}
.heading{font-family:Poppins,sans-serif;font-weight:600;color:var(--navy)}
.btn{position:absolute;display:flex;align-items:center;justify-content:center;gap:8px;background:var(--green);color:var(--white);font-family:Poppins,sans-serif;font-weight:600;font-size:11px;height:36px;letter-spacing:.2px}
.btn svg{width:18px;height:8px}
.stripes{display:inline-block;height:9px;background:repeating-linear-gradient(to bottom,var(--navy) 0 1px,transparent 1px 3px)}
.stripes.light{background:repeating-linear-gradient(to bottom,var(--white) 0 1px,transparent 1px 3px)}

/* header */
.site-header{position:absolute;top:0;left:0;width:1200px;height:64px;background:var(--white)}
.brand{position:absolute;left:121px;top:10px;font-family:Poppins,sans-serif;font-weight:600;color:#5f7785}
.brand .name{font-size:30px;line-height:32px;letter-spacing:3px}
.brand .sub{font-size:8px;letter-spacing:2.6px;color:var(--green);font-weight:500}
.nav a{position:absolute;top:25px;font-size:12px;color:var(--navy);text-decoration:none}
.nav a.active{color:var(--green)}
.phone{position:absolute;left:961px;top:21px;display:flex;gap:6px;align-items:center;color:var(--green);font-family:Poppins,sans-serif;font-weight:500;font-size:17px}

/* hero */
.hero{position:absolute;top:64px;left:0;width:1200px;height:463px;background:linear-gradient(100deg,#0c2530 0%,#173a44 35%,#3b3a33 58%,#8a5a32 72%,#6b6e72 85%,#3c4448 100%)}
.hero-welcome{left:122px;top:114px;font-size:12px;color:var(--green);display:flex;align-items:center;gap:6px}
.hero-welcome i{display:block;width:62px;height:1px;background:var(--green)}
.hero-name{left:120px;top:128px;font-family:Poppins,sans-serif;font-weight:500;font-size:104px;line-height:100px;letter-spacing:10px;color:var(--white)}
.hero-title{left:120px;top:238px;font-family:Poppins,sans-serif;font-weight:600;font-size:34px;color:var(--white);letter-spacing:.5px}
.hero-tag{left:122px;top:287px;font-size:13px;color:var(--white)}

/* about */
.about-frame{left:116px;top:589px;width:262px;height:250px;border-left:9px solid transparent;border-top:9px solid transparent;border-image:repeating-linear-gradient(90deg,#8a9499 0 1px,transparent 1px 3px) 9}
.about-lines{left:116px;top:589px;width:262px;height:250px}
.about-photo{left:139px;top:607px;width:411px;height:320px;background:linear-gradient(160deg,#cfd4d6,#8d969b 60%,#5c6468)}
.years-box{left:450px;top:698px;width:166px;height:138px;background:var(--green);outline:1px solid var(--green);outline-offset:3px;color:var(--white);text-align:center;padding-top:18px}
.years-box b{display:block;font-family:Poppins,sans-serif;font-weight:500;font-size:48px;line-height:52px}
.years-box span{font-size:17px;line-height:19px}
.about-label{left:689px;top:609px;font-size:11px;color:var(--green);display:flex;align-items:center;gap:5px}
.about-label i{display:block;width:46px;height:1px;background:var(--green)}
.about-bar{left:670px;top:638px;width:8px;height:60px;background:repeating-linear-gradient(90deg,#8a9499 0 1px,transparent 1px 3px)}
.about-heading{left:688px;top:628px;font-size:30px;line-height:36px}
.about-heading em{font-style:normal;color:var(--green)}
.about-text{left:689px;top:720px;width:365px;font-size:11px;line-height:15.7px}
.about-text p+p{margin-top:15px}

/* services */
.services{position:absolute;top:991px;left:0;width:1200px;height:620px;background:var(--mint)}
.section-title{position:absolute;left:0;width:1200px;text-align:center;font-size:30px;display:flex;justify-content:center;align-items:center;gap:6px}
.card{position:absolute;top:110px;width:307px}
.card-photo{height:297px;border:1px solid var(--navy);padding:3px;background:var(--white)}
.card-photo div{width:100%;height:100%}
.card-band{height:46px;background:var(--navy);color:var(--white);font-family:Poppins,sans-serif;font-weight:600;font-size:15px;padding:10px 18px}
.card-text{padding:12px 19px 0;font-size:10.8px;line-height:15px;height:56px}
.card .btn{position:relative;margin-left:19px;width:127px}

/* why */
.stat{position:absolute;top:1730px;display:flex;align-items:center;gap:18px}
.stat-circle{width:131px;height:131px}
.stat b{display:block;font-family:Poppins,sans-serif;font-weight:600;font-size:50px;line-height:50px;color:var(--green)}
.stat span{font-size:17px;color:var(--navy)}

/* cta */
.cta{position:absolute;top:1926px;left:0;width:1200px;height:259px;background:var(--green);text-align:center;color:var(--white)}
.cta h2{position:absolute;left:0;top:48px;width:1200px;font-family:Poppins,sans-serif;font-weight:600;font-size:31px;line-height:34px}
.cta h2 .row{display:flex;justify-content:center;align-items:center;gap:8px}
.cta p{position:absolute;left:0;top:124px;width:1200px;font-family:Poppins,sans-serif;font-weight:600;font-size:17px}

/* footer */
.site-footer{position:absolute;top:2185px;left:0;width:1200px;height:236px;background:var(--navy);color:#cfd8dd}
.foot-brand{left:122px;top:40px;font-family:Poppins,sans-serif;font-weight:600;color:#a9bcc6}
.foot-brand .name{font-size:30px;letter-spacing:3px;line-height:32px}
.foot-brand .sub{font-size:8px;letter-spacing:2.6px;color:var(--green)}
.foot-about{left:123px;top:117px;width:185px;font-size:9px;line-height:15.7px}
.divider{top:37px;width:1px;height:153px;background:#51687a}
.foot-head{top:40px;font-family:Poppins,sans-serif;font-weight:600;font-size:16px;color:var(--green)}
.foot-item{display:flex;align-items:center;gap:8px;font-size:9px}
.foot-item .ic{width:17px;height:17px;border-radius:50%;background:var(--white);display:flex;align-items:center;justify-content:center}
.foot-links{left:707px;top:77px;font-size:9px;line-height:17.5px}
.foot-rule{left:120px;top:195px;width:955px;height:1px;background:#51687a}
.copyright{left:0;top:211px;width:1200px;text-align:center;font-size:9px}
</style>
</head>
<body>

<header class="site-header">
  <div class="brand"><div class="name">KORVAL</div><div class="sub">PRECISION MACHINISTS</div></div>
  <nav class="nav">
    <a class="active" style="left:292px">HOME</a>
    <a style="left:357px">ABOUT US</a>
    <a style="left:446px">CNC MACHINING</a>
    <a style="left:571px">EDM WIRE CUTTING</a>
    <a style="left:712px">3D METAL PRINTING</a>
    <a style="left:858px">CONTACT US</a>
  </nav>
  <div class="phone">
    <svg width="16" height="16" viewBox="0 0 24 24"><path fill="currentColor" d="M6.6 10.8a15 15 0 0 0 6.6 6.6l2.2-2.2c.3-.3.7-.4 1-.2 1.1.4 2.3.6 3.6.6.6 0 1 .4 1 1V20c0 .6-.4 1-1 1A17 17 0 0 1 3 4c0-.6.4-1 1-1h3.5c.6 0 1 .4 1 1 0 1.3.2 2.5.6 3.6.1.3 0 .7-.2 1z"/></svg>
    1234567891
  </div>
</header>

<section class="hero" role="img" aria-label="Close-up of a lathe spindle throwing sparks while cutting metal">
  <div class="abs hero-welcome">WELCOME TO <i></i></div>
  <div class="abs hero-name">KORVAL</div>
  <div class="abs hero-title">Precision Machinists</div>
  <div class="abs hero-tag">We are a Mechanical Engineeringing Company</div>
  <a class="btn" style="left:121px;top:325px;width:128px">GET STARTED <svg viewBox="0 0 18 8"><path d="M0 4h16M13 1l3 3-3 3" stroke="#fff" fill="none"/></svg></a>
</section>

<section class="about">
  <svg class="abs about-lines" viewBox="0 0 262 250" aria-hidden="true">
    <g stroke="#8a9499" fill="none" stroke-width="1">
      <path d="M0.5 250V0.5H262"/><path d="M3.5 250V3.5H262"/><path d="M6.5 250V6.5H262"/><path d="M9.5 250V9.5H262"/><path d="M12.5 250V12.5H262"/><path d="M15.5 250V15.5H262"/>
    </g>
  </svg>
  <div class="abs about-photo" role="img" aria-label="Machinists working at benches in a CNC workshop"></div>
  <div class="abs years-box"><b>20+</b><span>Years of<br>Experience</span></div>
  <div class="abs about-label">ABOUT KORVAL PRECISION MACHINISTS <i></i></div>
  <div class="abs about-bar"></div>
  <h2 class="abs heading about-heading">We are a <em>Mechanical</em><br>Engineeringing Company</h2>
  <div class="abs about-text">
    <p>Based in Melbourne, EDM, CNC and 3D Metal Printing Services offers over twenty years of experience to the Mechanical Engineering Company. With our combination of highly skilled staff and sophisticated machinery we offer a comprehensive and professional service.</p>
    <p>The company has established itself as an efficient supplier of precision components and assemblies to end users within the manufacturing field and has the diversity to handle production runs as well single unit prototype work.</p>
  </div>
  <a class="btn" style="left:689px;top:877px;width:113px">READ MORE <svg viewBox="0 0 18 8"><path d="M0 4h16M13 1l3 3-3 3" stroke="#fff" fill="none"/></svg></a>
</section>

<section class="services">
  <h2 class="heading section-title" style="top:50px"><i class="stripes" style="width:60px"></i>Our Services<i class="stripes" style="width:60px"></i></h2>

  <div class="card" style="left:122px">
    <div class="card-photo"><div role="img" aria-label="Press brake bending a steel sheet" style="background:linear-gradient(160deg,#6b4a40,#8e8a86 55%,#4a4442)"></div></div>
    <div class="card-band">CNC Machining (5-axis, 3-axis)</div>
    <div class="card-text">With our combination of high quality Hollen Machining Centres we are able to provide innovative solutions to your precision CNC</div>
    <a class="btn">LEARN MORE <svg viewBox="0 0 18 8"><path d="M0 4h16M13 1l3 3-3 3" stroke="#fff" fill="none"/></svg></a>
  </div>

  <div class="card" style="left:447px">
    <div class="card-photo"><div role="img" aria-label="EDM wire cutting machine head over a workpiece" style="background:linear-gradient(170deg,#2a2a2c,#6d6e70 50%,#252526)"></div></div>
    <div class="card-band">EDM Wire cutting</div>
    <div class="card-text">We operate Swiss manufactured Vestrand EDM Machines which are regarded as the Starling Royale of wire cut machines.</div>
    <a class="btn">LEARN MORE <svg viewBox="0 0 18 8"><path d="M0 4h16M13 1l3 3-3 3" stroke="#fff" fill="none"/></svg></a>
  </div>

  <div class="card" style="left:771px">
    <div class="card-photo"><div role="img" aria-label="Brass laser nozzle of a metal 3D printer" style="background:linear-gradient(150deg,#9ea3a6,#b8944a 45%,#555a5d)"></div></div>
    <div class="card-band">3D Metal Printing</div>
    <div class="card-text">For the most part, aluminum is the primary alloy used in metal 3D printing. This is due to its high flexibility,</div>
    <a class="btn">LEARN MORE <svg viewBox="0 0 18 8"><path d="M0 4h16M13 1l3 3-3 3" stroke="#fff" fill="none"/></svg></a>
  </div>
</section>

<section class="why">
  <h2 class="heading section-title" style="top:1662px"><i class="stripes" style="width:60px"></i>Why Choose Us<i class="stripes" style="width:60px"></i></h2>

  <div class="stat" style="left:123px">
    <svg class="stat-circle" viewBox="0 0 131 131" aria-hidden="true">
      <circle cx="65.5" cy="65.5" r="64.5" fill="#fff" stroke="#0f2a3c"/>
      <g stroke="#0f2a3c"><path d="M10 102h111M13 106h105M17 110h97M22 114h87"/></g>
      <rect x="35" y="55" width="61" height="40" rx="3" fill="none" stroke="#0f2a3c" stroke-width="2.5"/>
      <path d="M54 55v-7h23v7M35 70h61" fill="none" stroke="#0f2a3c" stroke-width="2.5"/>
      <rect x="62" y="66" width="7" height="9" rx="1" fill="#34bc8a" stroke="#0f2a3c"/>
    </svg>
    <div><b>20+</b><span>Years of Experience</span></div>
  </div>

  <div class="stat" style="left:465px">
    <svg class="stat-circle" viewBox="0 0 131 131" aria-hidden="true">
      <circle cx="65.5" cy="65.5" r="64.5" fill="#fff" stroke="#0f2a3c"/>
      <g stroke="#0f2a3c"><path d="M10 102h111M13 106h105M17 110h97M22 114h87"/></g>
      <circle cx="66" cy="73" r="8" fill="#34bc8a" stroke="#0f2a3c" stroke-width="2"/>
      <circle cx="46" cy="78" r="6" fill="none" stroke="#0f2a3c" stroke-width="2"/>
      <circle cx="86" cy="78" r="6" fill="none" stroke="#0f2a3c" stroke-width="2"/>
      <path d="M52 100a14 14 0 0 1 28 0M34 100a12 12 0 0 1 20-8M98 100a12 12 0 0 0-20-8" fill="none" stroke="#0f2a3c" stroke-width="2"/>
      <path d="M66 40l3 6 6 1-4 4 1 6-6-3-6 3 1-6-4-4 6-1z" fill="none" stroke="#0f2a3c" stroke-width="1.6"/>
      <path d="M46 52l2 4 4 .5-3 3 .8 4-3.8-2-3.8 2 .8-4-3-3 4-.5zM86 52l2 4 4 .5-3 3 .8 4-3.8-2-3.8 2 .8-4-3-3 4-.5z" fill="none" stroke="#0f2a3c" stroke-width="1.4"/>
    </svg>
    <div><b>1000+</b><span>Happy Customers</span></div>
  </div>

  <div class="stat" style="left:803px">
    <svg class="stat-circle" viewBox="0 0 131 131" aria-hidden="true">
      <circle cx="65.5" cy="65.5" r="64.5" fill="#fff" stroke="#0f2a3c"/>
      <g stroke="#0f2a3c"><path d="M10 102h111M13 106h105M17 110h97M22 114h87"/></g>
      <path d="M32 76h12v24H32zM44 78l12-14 3-10c4 0 6 4 4 10l-2 6h14c4 0 5 5 1 6 3 1 3 5 0 6 2 1 2 5-1 6 1 1 1 4-2 5H48l-4-2" fill="none" stroke="#0f2a3c" stroke-width="2"/>
      <rect x="68" y="36" width="32" height="22" rx="3" fill="none" stroke="#0f2a3c" stroke-width="2"/>
      <path d="M78 58l-3 6 8-6" fill="none" stroke="#0f2a3c" stroke-width="2"/>
      <circle cx="84" cy="47" r="7" fill="#34bc8a" stroke="#0f2a3c"/>
      <path d="M81 47l2 2 4-4" stroke="#0f2a3c" stroke-width="1.6" fill="none"/>
    </svg>
    <div><b>500+</b><span>Trusted Reviews</span></div>
  </div>
</section>

<section class="cta">
  <h2><span class="row"><i class="stripes light" style="width:60px"></i>Start running a more<i class="stripes light" style="width:60px"></i></span>Profitable CNC machine Shop.</h2>
  <p>Today with Korval Precision Machinists</p>
  <a class="btn" style="left:533px;top:162px;width:135px;background:var(--navy)">GET STARTED <svg viewBox="0 0 18 8"><path d="M0 4h16M13 1l3 3-3 3" stroke="#fff" fill="none"/></svg></a>
</section>

<footer class="site-footer">
  <div class="abs foot-brand"><div class="name">KORVAL</div><div class="sub">PRECISION MACHINISTS</div></div>
  <p class="abs foot-about">Based in Melbourne, EDM, CNC and 3D Metal Printing Services offers over twenty years of experience to the Mechanical Engineering Company.</p>

  <div class="abs divider" style="left:362px"></div>
  <div class="abs divider" style="left:627px"></div>
  <div class="abs divider" style="left:876px"></div>

  <h3 class="abs foot-head" style="left:412px">Contact Us</h3>
  <div class="abs foot-item" style="left:414px;top:76px"><span class="ic"><svg width="10" height="10" viewBox="0 0 24 24"><path fill="#0f2a3c" d="M6.6 10.8a15 15 0 0 0 6.6 6.6l2.2-2.2c.3-.3.7-.4 1-.2 1.1.4 2.3.6 3.6.6.6 0 1 .4 1 1V20c0 .6-.4 1-1 1A17 17 0 0 1 3 4c0-.6.4-1 1-1h3.5c.6 0 1 .4 1 1 0 1.3.2 2.5.6 3.6.1.3 0 .7-.2 1z"/></svg></span>1234567891</div>
  <div class="abs foot-item" style="left:414px;top:109px"><span class="ic"><svg width="10" height="8" viewBox="0 0 20 14"><rect width="20" height="14" rx="2" fill="#0f2a3c"/><path d="M1 1l9 7 9-7" stroke="#fff" fill="none" stroke-width="1.5"/></svg></span>info@korvalprecision.com</div>

  <h3 class="abs foot-head" style="left:706px">About Us</h3>
  <div class="abs foot-links">Home<br>About Us<br>CNC Machining<br>EDM Wire cutting<br>3D Metal Printing<br>Contact Us</div>

  <h3 class="abs foot-head" style="left:958px">follow us</h3>
  <div class="abs foot-item" style="left:960px;top:77px"><span class="ic"></span>Facelink</div>
  <div class="abs foot-item" style="left:960px;top:107px"><span class="ic"></span>Pictagram</div>
  <div class="abs foot-item" style="left:960px;top:137px"><span class="ic"></span>Chirper</div>

  <div class="abs foot-rule"></div>
  <div class="abs copyright">© 2024 Korval Precision Machinists. All rights reserved.</div>
</footer>

</body>
</html>
```